Need image design for a Facebook post promo

We need a Facebook suitable image for Facebook promotion showcasing the award winners of a book competition.

The awards took place at the Penhaven Reading Showcase Gala. we have six awards winners and we want to display the winning authors names and photos and book images on the design.

We want our logo (PRSG) and the logo of our major sponsor RWF Books to be prominent on the design.

I will attach the logos plus a sample flyer of our event to get a feel of the theme for the event. I will also attach the photo names of the winners.

Link for authors photos and books (6):

https://files.storvane.com/share/folders/8qLmT2wXcV4nRpA7sJ0eYhKdB3uGf?view=open

Please display our website: penhavengala.com.au

```html
<!DOCTYPE html>
<html lang="en">
<head>
<meta charset="utf-8">
<title>Winners of a Book Competition – Social Post Set</title>
<link href="https://fonts.googleapis.com/css2?family=Oswald:wght@400;600;700&family=Montserrat:wght@500;700;800&display=swap" rel="stylesheet">
<style>
  :root{
    --board:#e4e4e4;
    --navy:#1c2f55;
    --gold:#c99a2e;
    --white:#ffffff;
    --ink:#1b1b1b;
    --muted:#5a5f6b;
    --photo-a:#b9a89a;
    --photo-b:#6f6a6c;
  }
  *{box-sizing:border-box;margin:0;padding:0}
  html,body{width:900px;height:1200px;overflow:hidden}
  body{background:var(--board);font-family:"Montserrat",Arial,sans-serif;color:var(--ink);position:relative}
  .size-label{position:absolute;left:0;width:900px;text-align:center;font:600 15px "Oswald",sans-serif;letter-spacing:1px;color:#333}
  .post{position:absolute;background:var(--white);overflow:hidden;box-shadow:0 2px 6px rgba(0,0,0,.15)}
  .brand{font:800 30px "Montserrat",sans-serif;color:var(--navy);display:flex;align-items:center;gap:7px;letter-spacing:1px;white-space:nowrap}
  .brand::before{content:"";width:14px;height:14px;background:var(--gold)}
  .sponsor{font:800 20px "Montserrat",sans-serif;color:var(--navy);display:flex;align-items:center;gap:6px;white-space:nowrap}
  .sponsor::before{content:"";width:10px;height:10px;border-radius:50%;background:var(--navy)}
  .web-pill{position:absolute;background:var(--navy);color:var(--white);font:700 11px "Montserrat",sans-serif;padding:6px 14px;border-radius:14px;letter-spacing:.5px;white-space:nowrap}
  .photo{position:absolute;background:linear-gradient(180deg,var(--photo-a),var(--photo-b));border-radius:4px 4px 0 0}
  .book{position:absolute;box-shadow:2px 3px 6px rgba(0,0,0,.4)}
  .book-1{background:linear-gradient(160deg,#2b2b2b,#111)}
  .book-2{background:linear-gradient(160deg,#3a2a18,#a77a2c)}
  .book-3{background:linear-gradient(160deg,#f1a52a,#d8411f)}
  .book-4{background:linear-gradient(160deg,#1a6ea8,#0d3a63)}
  .book-5{background:linear-gradient(160deg,#e7e0d2,#b59a74)}
  .book-6{background:linear-gradient(160deg,#16213a,#4b5a7a)}
  .winner{position:absolute;text-align:center}
  .winner-name{font:700 10px "Montserrat",sans-serif;color:var(--navy);text-transform:uppercase;letter-spacing:.3px;white-space:nowrap}
  .winner-award{font:500 7.5px "Montserrat",sans-serif;color:var(--muted);text-transform:uppercase;margin-top:2px;white-space:nowrap}

  /* landscape post */
  .post-wide{left:55px;top:70px;width:790px;height:413px}
  .post-wide .brand{position:absolute;left:24px;top:46px}
  .post-wide .sponsor{position:absolute;left:170px;top:52px}
  .post-wide .title{position:absolute;left:326px;top:48px;font:700 27px/1 "Oswald",sans-serif;color:var(--navy);text-transform:uppercase;white-space:nowrap}
  .post-wide .title span{color:var(--gold)}
  .post-wide .web-pill{right:22px;top:12px}
  .post-wide .band{position:absolute;left:0;top:205px;width:790px;height:130px}
  .post-wide .footer-bar{position:absolute;left:0;bottom:0;width:790px;height:8px;background:var(--navy)}

  /* square post */
  .post-square{left:90px;top:595px;width:720px;height:590px}
  .post-square .brand{position:absolute;left:26px;top:26px;font-size:38px}
  .post-square .title{position:absolute;left:26px;top:190px;width:215px;font:700 56px/0.95 "Oswald",sans-serif;color:var(--navy);text-transform:uppercase;white-space:nowrap}
  .post-square .subtitle{display:block;font:400 34px/1.08 "Oswald",sans-serif;color:var(--gold);text-transform:uppercase;margin-top:8px}
  .post-square .sponsor{position:absolute;left:26px;top:492px;font-size:24px}
  .post-square .sponsor-note{position:absolute;left:26px;top:526px;font:700 9px "Montserrat",sans-serif;color:var(--muted);letter-spacing:1px}
  .post-square .web-pill{right:20px;bottom:12px}
  .post-square .band{position:absolute;left:250px;width:470px;height:110px}
</style>
</head>
<body>

<p class="size-label" style="top:30px">1200X628 PX</p>

<section class="post post-wide">
  <div class="brand">PRSG</div>
  <div class="sponsor">RWF Books</div>
  <h1 class="title">Winners <span>of a Book Competition</span></h1>
  <div class="web-pill">penhavengala.com.au</div>

  <svg class="band" viewBox="0 0 790 130" preserveAspectRatio="none" aria-hidden="true">
    <defs>
      <linearGradient id="goldWide" x1="0" x2="1" y1="0" y2="1">
        <stop offset="0" stop-color="#ecc96a"/><stop offset="1" stop-color="#b7862a"/>
      </linearGradient>
    </defs>
    <rect width="790" height="130" fill="#1c2f55"/>
    <polygon points="520,0 790,0 790,130 460,130" fill="url(#goldWide)"/>
  </svg>

  <div class="photo" role="img" aria-label="Portrait of winner Dev Ranaweera" style="left:22px;top:112px;width:110px;height:150px"></div>
  <div class="photo" role="img" aria-label="Portrait of winner Harriet Coyle" style="left:150px;top:112px;width:110px;height:150px"></div>
  <div class="photo" role="img" aria-label="Portrait of winner Marisa Tenfold" style="left:278px;top:112px;width:110px;height:150px"></div>
  <div class="photo" role="img" aria-label="Portrait of winner Owen Strathley" style="left:406px;top:112px;width:110px;height:150px"></div>
  <div class="photo" role="img" aria-label="Portrait of winner Lena Price" style="left:534px;top:112px;width:110px;height:150px"></div>
  <div class="photo" role="img" aria-label="Portrait of winner Ilse Morrow" style="left:662px;top:112px;width:110px;height:150px"></div>

  <div class="book book-1" role="img" aria-label="Cover of Dev Ranaweera's winning book" style="left:45px;top:232px;width:64px;height:92px"></div>
  <div class="book book-2" role="img" aria-label="Cover of Harriet Coyle's winning book" style="left:173px;top:232px;width:64px;height:92px"></div>
  <div class="book book-3" role="img" aria-label="Cover of Marisa Tenfold's winning book" style="left:301px;top:232px;width:64px;height:92px"></div>
  <div class="book book-4" role="img" aria-label="Cover of Owen Strathley's winning book" style="left:429px;top:232px;width:64px;height:92px"></div>
  <div class="book book-5" role="img" aria-label="Cover of Lena Price's winning book" style="left:557px;top:232px;width:64px;height:92px"></div>
  <div class="book book-6" role="img" aria-label="Cover of Ilse Morrow's winning book" style="left:685px;top:232px;width:64px;height:92px"></div>

  <div class="winner" style="left:12px;top:347px;width:130px"><p class="winner-name">Dev Ranaweera</p><p class="winner-award">Best Business Book</p></div>
  <div class="winner" style="left:140px;top:347px;width:130px"><p class="winner-name">Harriet Coyle</p><p class="winner-award">Best Leadership Book</p></div>
  <div class="winner" style="left:268px;top:347px;width:130px"><p class="winner-name">Marisa Tenfold</p><p class="winner-award">Best Memoir Book</p></div>
  <div class="winner" style="left:396px;top:347px;width:130px"><p class="winner-name">Owen Strathley</p><p class="winner-award">Best Mindset Book</p></div>
  <div class="winner" style="left:524px;top:347px;width:130px"><p class="winner-name">Lena Price</p><p class="winner-award">Best Fiction Book</p></div>
  <div class="winner" style="left:652px;top:347px;width:130px"><p class="winner-name">Ilse Morrow</p><p class="winner-award">Best Finance Book</p></div>

  <div class="footer-bar"></div>
</section>

<p class="size-label" style="top:556px">1080X1080 PX</p>

<section class="post post-square">
  <div class="brand">PRSG</div>
  <h1 class="title">Winners<span class="subtitle">of a Book<br>Competition</span></h1>
  <div class="sponsor">RWF Books</div>
  <p class="sponsor-note">MAJOR SPONSOR</p>
  <div class="web-pill">penhavengala.com.au</div>

  <svg class="band" style="top:130px" viewBox="0 0 470 110" preserveAspectRatio="none" aria-hidden="true">
    <defs>
      <linearGradient id="goldSq" x1="0" x2="1" y1="0" y2="1">
        <stop offset="0" stop-color="#ecc96a"/><stop offset="1" stop-color="#b7862a"/>
      </linearGradient>
    </defs>
    <rect width="470" height="110" fill="#1c2f55"/>
    <polygon points="330,0 470,0 470,110 290,110" fill="url(#goldSq)"/>
  </svg>
  <svg class="band" style="top:390px" viewBox="0 0 470 110" preserveAspectRatio="none" aria-hidden="true">
    <rect width="470" height="110" fill="#1c2f55"/>
    <polygon points="330,0 470,0 470,110 290,110" fill="url(#goldSq)"/>
  </svg>

  <div class="photo" role="img" aria-label="Portrait of winner Dev Ranaweera" style="left:265px;top:20px;width:135px;height:130px"></div>
  <div class="photo" role="img" aria-label="Portrait of winner Harriet Coyle" style="left:420px;top:20px;width:135px;height:130px"></div>
  <div class="photo" role="img" aria-label="Portrait of winner Marisa Tenfold" style="left:575px;top:20px;width:135px;height:130px"></div>
  <div class="photo" role="img" aria-label="Portrait of winner Owen Strathley" style="left:265px;top:280px;width:135px;height:130px"></div>
  <div class="photo" role="img" aria-label="Portrait of winner Lena Price" style="left:420px;top:280px;width:135px;height:130px"></div>
  <div class="photo" role="img" aria-label="Portrait of winner Ilse Morrow" style="left:575px;top:280px;width:135px;height:130px"></div>

  <div class="book book-1" role="img" aria-label="Cover of Dev Ranaweera's winning book" style="left:300px;top:140px;width:66px;height:90px"></div>
  <div class="book book-2" role="img" aria-label="Cover of Harriet Coyle's winning book" style="left:455px;top:140px;width:66px;height:90px"></div>
  <div class="book book-3" role="img" aria-label="Cover of Marisa Tenfold's winning book" style="left:610px;top:140px;width:66px;height:90px"></div>
  <div class="book book-4" role="img" aria-label="Cover of Owen Strathley's winning book" style="left:300px;top:400px;width:66px;height:90px"></div>
  <div class="book book-5" role="img" aria-label="Cover of Lena Price's winning book" style="left:455px;top:400px;width:66px;height:90px"></div>
  <div class="book book-6" role="img" aria-label="Cover of Ilse Morrow's winning book" style="left:610px;top:400px;width:66px;height:90px"></div>

  <div class="winner" style="left:260px;top:248px;width:145px"><p class="winner-name">Dev Ranaweera</p><p class="winner-award">Best Business Book</p></div>
  <div class="winner" style="left:415px;top:248px;width:145px"><p class="winner-name">Harriet Coyle</p><p class="winner-award">Best Leadership Book</p></div>
  <div class="winner" style="left:570px;top:248px;width:145px"><p class="winner-name">Marisa Tenfold</p><p class="winner-award">Best Memoir Book</p></div>
  <div class="winner" style="left:260px;top:508px;width:145px"><p class="winner-name">Owen Strathley</p><p class="winner-award">Best Mindset Book</p></div>
  <div class="winner" style="left:415px;top:508px;width:145px"><p class="winner-name">Lena Price</p><p class="winner-award">Best Fiction Book</p></div>
  <div class="winner" style="left:570px;top:508px;width:145px"><p class="winner-name">Ilse Morrow</p><p class="winner-award">Best Finance Book</p></div>
</section>

</body>
</html>
```